Pactwise - Training I Consulting I Review - Related to Contracts/Agreements

We provide legal services, we need a plattform to book video online trainings or local trainings classes and appointments (with calendar feature to select date and see availability at screen), payment over internet, legal document creation over webpage, videos will be produces in the next 3 - 4 moths so this is a place holder item. Participants for the Online trainings shall have a login in area with secured password. Appointments for local trainings and Consulting. Consider Outline in file attached. I can send you also a video with more explanation regarding the purpose.

Target Market(s)

Startup/scale up Software companies that intent to have an international business and need help with their contracts, to sell their products. Sales persons.

Industry/Entity Type

Legal

Coding

Coded - Design and coding required

Number of Pages Required

5+ page

Font styles to use
Serif
Sans Serif

Colors
000000
eeeeee
f5f5f5
ffffff
f8fcfd
3277b5
ecf7fb
cadf82
86cfc6

Requirements
Must have
• See file pactwise attached with outline. Moreover see here first starting point: https://moritz-ebbing.sitebuildr-demo.net/mysite-1 . Main inspiration comes from www.advisoryhub-demo.net from the log in area, see the outline in the file attached with the screen shots. At the end I need someone who can draft the full webpage and maintain it for a yearly fee. It must be simple and well structured layout. Lean. 1st landing page shall not scroll, 2 landing page only a little to see the testimonials and foster of page. There should be a Progress Bar to indicate the booking/selection process. Calendar booking. Easy fast booking.
• I like the colour mix, the feeling and the easy structor of:
• https://www.artpitch-demo.net/design/6374387or
• https://www.artpitch-demo.net/design/6372391 or https://www.artpitch-demo.net/design/6374366
• https://www.agencyfind-demo.net/en/web-design/belgium-be
• https://www.artpitch-demo.net/design/5896857
• https://www.artpitch-demo.net/design/5902173
• https://www.artpitch-demo.net/design/17197349
• https://www.artpitch-demo.net/design/5464461
• https://www.artpitch-demo.net/design/7180908
Nice to have
• page for evaluation and interview, see outline attached in the file with screen shots. Document upload.
Should not have
• many pictures, long scroll down pages on the 1st and 2nd ladding pages, many colours and forms. No need for news letter, search field, no need for links to Chatterly and other social media (except workNet).

```html
<!DOCTYPE html>
<html lang="en">
<head>
<meta charset="utf-8">
<title>Pactwise – Book Now</title>
<link href="https://fonts.googleapis.com/css2?family=Mulish:wght@400;500;600&family=Merriweather:wght@700&display=swap" rel="stylesheet">
<style>
:root{
  --dark:#333333;
  --accent:#7ecbe4;
  --page:#f5f5f5;
  --white:#ffffff;
  --text:#222222;
  --muted:#9a9a9a;
  --line:#d4d4d4;
  --event:#1a6fc0;
  --event-faded:#86b6de;
}
*{box-sizing:border-box;margin:0;padding:0}
html,body{width:1200px;height:1111px;overflow:hidden}
body{background:var(--page);font-family:"Mulish",Arial,sans-serif;color:var(--text);position:relative}
.abs{position:absolute}

/* header */
.site-header{position:absolute;left:0;top:0;width:1200px;height:62px;background:var(--dark);border-bottom:2px solid var(--accent)}
.brand{position:absolute;left:150px;top:14px;font-size:28px;font-weight:400;color:var(--white);letter-spacing:1px;line-height:32px}
.main-nav a{position:absolute;top:0;height:62px;line-height:64px;color:var(--white);font-size:15px;font-weight:500;text-decoration:none;text-align:center}
.main-nav a.active{background:var(--accent)}
.login-btn{position:absolute;left:931px;top:16px;width:112px;height:33px;background:var(--accent);color:var(--white);font-size:14px;display:flex;align-items:center;justify-content:center;gap:5px;border-radius:2px}

/* headings */
.page-title{left:0;width:1200px;top:120px;text-align:center;font-size:27px;font-weight:400}
.section-title{left:0;width:1200px;text-align:center;font-size:19px;font-weight:400}

/* tabs */
.booking-tabs{left:308px;top:189px;width:584px;height:31px;display:flex}
.booking-tabs div{flex:1;color:var(--white);font-size:14.5px;font-weight:500;padding-left:14px;line-height:31px;position:relative}
.tab-class{background:var(--accent)}
.tab-online{background:var(--dark)}
.tab-class::after{content:"";position:absolute;left:20px;bottom:-7px;border-left:7px solid transparent;border-right:7px solid transparent;border-top:7px solid var(--accent)}

/* perks */
.perk{font-size:14.5px;display:flex;align-items:center;gap:6px;white-space:nowrap}
.perk em{font-style:normal;color:var(--accent)}
.sep{width:1px;height:13px;background:var(--line)}

/* calendar */
.calendar{left:308px;top:396px;width:584px;height:241px;background:var(--white);overflow:hidden;border:1px solid #e6e6e6}
.cal-nav{position:absolute;top:22px;font-size:15px;color:var(--accent)}
.cal-month{position:absolute;top:20px;left:0;width:575px;text-align:center;font-size:16px}
.cal-grid{position:absolute;left:11px;top:60px;width:550px;display:grid;grid-template-columns:repeat(7,1fr);border-left:1px solid var(--line);border-top:1px solid var(--line)}
.cal-grid .dow{background:#e4e4e4;font-family:"Merriweather",Georgia,serif;font-size:7px;font-weight:700;text-align:center;height:16px;line-height:16px;border-right:1px solid var(--line);border-bottom:1px solid var(--line);letter-spacing:.5px}
.cal-grid .day{height:60px;border-right:1px solid var(--line);border-bottom:1px solid var(--line);font-size:6.5px;position:relative}
.day .num{display:block;background:#f2f2f2;height:13px;line-height:13px;padding-left:5px;font-weight:600}
.day.other .num{color:var(--muted)}
.day .ev{display:block;color:var(--event);padding:4px 8px 0;line-height:9px;font-size:7px}
.day.other .ev{color:var(--event-faded)}
.scrollbar{position:absolute;right:0;top:0;width:9px;height:100%;background:#efefef}
.scrollbar span{position:absolute;left:3px;top:60px;width:3px;height:30px;background:var(--accent);border-radius:2px}

/* form */
.field-label{font-size:14.5px}
.field-input{height:31px;background:var(--page);border:1px solid #cfcfcf;font-size:11.5px;color:#b5b5b5;padding-left:10px;line-height:29px;border-radius:2px}
.payment{left:306px;top:886px;font-size:14.5px;display:flex;align-items:center;gap:12px}
.radio{display:inline-flex;align-items:center;gap:7px;color:#666}
.radio i{width:11px;height:11px;border:1px solid #888;border-radius:50%;display:inline-block;position:relative}
.radio.checked{color:var(--accent)}
.radio.checked i{border-color:var(--accent)}
.radio.checked i::after{content:"";position:absolute;left:2px;top:2px;width:5px;height:5px;border-radius:50%;background:var(--accent)}
.pipe{color:#666}
.submit-btn{left:543px;top:933px;width:113px;height:34px;background:var(--accent);color:var(--white);font-size:13px;text-align:center;line-height:34px;border-radius:2px}

/* footer */
.site-footer{left:0;top:1031px;width:1200px;height:80px;background:var(--dark);color:var(--white);font-size:13px;text-align:center}
.footer-links{position:absolute;top:15px;width:100%}
.footer-links a{color:var(--white);text-decoration:none;margin:0 10px}
.footer-links a.current{color:var(--accent);text-decoration:underline}
.copyright{position:absolute;top:45px;width:100%}
.copyright span{color:var(--accent)}
</style>
</head>
<body>

<header class="site-header">
  <div class="brand">Pactwise</div>
  <nav class="main-nav">
    <a href="#" style="left:426px;width:130px">Refere Someone</a>
    <a href="#" class="active" style="left:574px;width:114px">Services</a>
    <a href="#" style="left:700px;width:80px">Partner</a>
    <a href="#" style="left:808px;width:80px">Contact</a>
  </nav>
  <div class="login-btn">
    <svg width="8" height="11" viewBox="0 0 8 11"><circle cx="4" cy="2.7" r="2.5" fill="#fff"/><path d="M0 11v-2.5a4 3 0 0 1 8 0V11z" fill="#fff"/></svg>
    Login
  </div>
</header>

<h1 class="abs page-title">Book Now!</h1>

<div class="abs booking-tabs">
  <div class="tab-class">Book Class</div>
  <div class="tab-online">Book Online</div>
</div>

<svg width="0" height="0" style="position:absolute">
  <symbol id="tick" viewBox="0 0 12 12"><rect x="0.5" y="1.5" width="10" height="10" fill="none" stroke="#7ecbe4"/><path d="M3 6l2.5 2.5L11 2" fill="none" stroke="#7ecbe4" stroke-width="1.3"/></symbol>
</svg>

<div class="abs perk" style="left:308px;top:264px"><svg width="12" height="12"><use href="#tick"/></svg><span>Seat Availability <em>Limited</em></span></div>
<div class="abs sep" style="left:527px;top:268px"></div>
<div class="abs perk" style="left:547px;top:264px"><svg width="12" height="12"><use href="#tick"/></svg><span>Grab <em>10% Discount</em> on Class Training</span></div>
<div class="abs perk" style="left:308px;top:289px"><svg width="12" height="12"><use href="#tick"/></svg><span>Local Training for <em>Clients</em> and <em>Students</em></span></div>
<div class="abs sep" style="left:615px;top:293px"></div>
<div class="abs perk" style="left:635px;top:289px"><svg width="12" height="12"><use href="#tick"/></svg><span>Discounted Price for <em>Students</em></span></div>

<h2 class="abs section-title" style="top:345px">Select From Available Date &amp; Time</h2>

<section class="abs calendar">
  <div class="cal-nav" style="left:15px">« March</div>
  <div class="cal-month">April 2018</div>
  <div class="cal-nav" style="left:516px">May »</div>
  <div class="cal-grid">
    <div class="dow">SUNDAY</div><div class="dow">MONDAY</div><div class="dow">TUESDAY</div><div class="dow">WEDNESDAY</div><div class="dow">THURSDAY</div><div class="dow">FRIDAY</div><div class="dow">SATURDAY</div>
    <div class="day other"><span class="num">26</span></div>
    <div class="day other"><span class="num">27</span></div>
    <div class="day other"><span class="num">28</span><span class="ev">Children's Petting Zoo</span></div>
    <div class="day other"><span class="num">29</span><span class="ev">Movie Marathon</span></div>
    <div class="day other"><span class="num">30</span></div>
    <div class="day"><span class="num">1</span><span class="ev">80's Dance Party</span></div>
    <div class="day"><span class="num">2</span><span class="ev">Cupcake Decorating</span></div>
    <div class="day"><span class="num">3</span><span class="ev">Cupcake Eating Contest</span></div>
    <div class="day"><span class="num">4</span></div>
    <div class="day"><span class="num">5</span></div>
    <div class="day"><span class="num">6</span><span class="ev">Maple Developer Meetup</span></div>
    <div class="day"><span class="num">7</span></div>
    <div class="day"><span class="num">8</span><span class="ev">FutureTalk with Jon Avery</span></div>
    <div class="day"><span class="num">9</span></div>
    <div class="day"><span class="num">10</span></div>
    <div class="day"><span class="num">11</span></div>
    <div class="day"><span class="num">12</span><span class="ev">Oregon Science Startup Forum</span></div>
    <div class="day"><span class="num">13</span></div>
    <div class="day"><span class="num">14</span><span class="ev">Gallery Exhibit Opening</span></div>
    <div class="day"><span class="num">15</span></div>
    <div class="day"><span class="num">16</span><span class="ev">Farmer's Market</span><span class="ev">WebMeet Lyon</span></div>
  </div>
  <div class="scrollbar"><span></span></div>
</section>

<h2 class="abs section-title" style="top:680px">Fill Personal Details</h2>

<label class="abs field-label" style="left:306px;top:729px">Full Name:</label>
<div class="abs field-input" style="left:308px;top:756px;width:280px">Enter Your Full Name...</div>
<label class="abs field-label" style="left:611px;top:729px">Phone:</label>
<div class="abs field-input" style="left:612px;top:756px;width:280px">Enter Your Phone Number..</div>
<label class="abs field-label" style="left:306px;top:804px">Company Name :</label>
<div class="abs field-input" style="left:308px;top:830px;width:280px">Enter Your Company Name ...</div>
<label class="abs field-label" style="left:611px;top:804px">Email:</label>
<div class="abs field-input" style="left:612px;top:830px;width:280px">Enter Your Email Address...</div>

<div class="abs payment">
  <span>Select Payment Mode :</span>
  <span class="radio"><i></i>Credit Card</span><span class="pipe">|</span>
  <span class="radio checked"><i></i>Debit Card</span><span class="pipe">|</span>
  <span class="radio"><i></i>Paynesto</span>
</div>

<div class="abs submit-btn">Submit</div>

<footer class="abs site-footer">
  <div class="footer-links">
    <a href="#" class="current">Refere Someone</a>|<a href="#">Services</a>|<a href="#">Partner</a>|<a href="#">Team</a>|<a href="#">Contact</a>
  </div>
  <div class="copyright">© 2018 <span>Pactwise</span> &nbsp;|&nbsp; All Right Reserved.</div>
</footer>

</body>
</html>
```